Simple and Approachable Cover for Pet Expo Company Page

Size: 2000 x 430; looking simply for words "Tenbury HR Consulting" and email address "TenburyHRConsulting@mailvane.com." This is for a cover photo for a company profile page for the Northway Animal Fair, where I am a featured speaker on Employee Communications later this month. You can incorporate the attached photo to the left of the banner ad if you wish. The mood I wish to present is approachable, positive and simple.

Target Market(s)

small pet retail business owners

Industry/Entity Type

Pet Shop

Font styles to use
Serif
Sans Serif

Requirements
Must have
• Email address clearly defined/separated. Easy to read.
Nice to have
• I like the picture that I included; subtle pet paw background is also nice
Should not have
• No paid stock images

```html
<!DOCTYPE html>
<html lang="en">
<head>
<meta charset="utf-8">
<title>Tenbury HR Consulting — Cover</title>
<link rel="stylesheet" href="https://fonts.googleapis.com/css2?family=Lexend:wght@400;500&display=swap">
<style>
  :root {
    --ink-indigo: #2e3192;
    --accent-gold: #f2b51c;
    --brand-blue: #0b6dbd;
    --deep-blue: #0a5aa3;
    --sky-blue: #43a6de;
    --paper: #ffffff;
  }
  html, body {
    margin: 0;
    padding: 0;
    overflow: hidden;
    background: var(--paper);
  }
  .cover {
    position: relative;
    width: 1200px;
    height: 258px;
    overflow: hidden;
    background: var(--paper);
    font-family: "Lexend", sans-serif;
  }
  .cover__art {
    position: absolute;
    inset: 0;
  }
  .cover__title {
    position: absolute;
    left: 456px;
    width: 722px;
    top: 84px;
    margin: 0;
    font-size: 62px;
    font-weight: 500;
    line-height: 1;
    letter-spacing: 0;
    color: var(--ink-indigo);
    text-shadow: 2px 3px 0 var(--accent-gold);
    white-space: nowrap;
    text-align: right;
  }
  .contact-pill {
    position: absolute;
    left: 696px;
    top: 205px;
    width: 479px;
    height: 42px;
    border-radius: 6px;
    background: var(--brand-blue);
    display: flex;
    align-items: center;
  }
  .contact-pill__icon {
    margin-left: 3px;
    width: 38px;
    height: 38px;
    flex: none;
  }
  .contact-pill__email {
    margin-left: 16px;
    font-size: 22.5px;
    font-weight: 400;
    color: var(--paper);
    white-space: nowrap;
  }
</style>
</head>
<body>
  <div class="cover">
    <svg class="cover__art" width="1200" height="258" viewBox="0 0 1200 258">
      <defs>
        <linearGradient id="photoTone" x1="0" y1="0" x2="1" y2="1">
          <stop offset="0" stop-color="#6f7a4a"/>
          <stop offset="0.5" stop-color="#9a8a5c"/>
          <stop offset="1" stop-color="#5f6e3a"/>
        </linearGradient>
        <linearGradient id="waveTone" x1="0" y1="0" x2="1" y2="0">
          <stop offset="0" stop-color="#cfe4f6"/>
          <stop offset="0.6" stop-color="#eef5fc"/>
          <stop offset="1" stop-color="#ffffff"/>
        </linearGradient>
        <linearGradient id="chevronTone" x1="0" y1="0" x2="1" y2="1">
          <stop offset="0" stop-color="var(--sky-blue)"/>
          <stop offset="0.5" stop-color="var(--deep-blue)"/>
          <stop offset="1" stop-color="var(--sky-blue)"/>
        </linearGradient>
      </defs>
      <rect class="wave-field" role="img" aria-label="Soft flowing line pattern with faint paw prints" x="330" y="0" width="570" height="258" fill="url(#waveTone)"/>
      <polygon class="hero-photo" role="img" aria-label="Photo of the consultants seated on grass in a park with their two dogs" points="0,0 270,0 410,129 262,258 0,258" fill="url(#photoTone)"/>
      <polygon class="chevron-band" points="264,0 330,0 444,129 366,258 256,258 410,129" fill="url(#chevronTone)"/>
    </svg>

    <h1 class="cover__title">Tenbury HR Consulting</h1>

    <div class="contact-pill">
      <svg class="contact-pill__icon" viewBox="0 0 38 38" aria-hidden="true">
        <circle cx="19" cy="19" r="17.5" fill="var(--paper)" stroke="var(--accent-gold)" stroke-width="2.5"/>
        <rect x="10" y="13" width="18" height="12" fill="none" stroke="var(--accent-gold)" stroke-width="1.8"/>
        <polyline points="10,13 19,20 28,13" fill="none" stroke="var(--accent-gold)" stroke-width="1.8"/>
      </svg>
      <span class="contact-pill__email">TenburyHRConsulting@mailvane.com</span>
    </div>
  </div>
</body>
</html>
```